Dental Business Card

I need Dental oriented business cards.
On the front side -
- on the first line, my name:
Dr Marlo Vintner
- on the second line (just underneath):
Doctor of Dental Medicine
- on the third line, or underneath that or in a corner, I would like the address and phone number:
5182 Ch. Birchfield
Montreal QC H2T 4B9
514-629-5074
- other than that i would maybe like a logo of a tooth, but i want it to be subtle and very basic!
- I would like the card to be preferably black or dark grey-ish with the writing in white
On the other side -
- 2-3 lines with the possibility to write the next appointment the box with the lines should be white, with the rest of the card being black

```html
<!DOCTYPE html>
<html lang="en">
<head>
<meta charset="utf-8">
<title>Vintner Dental – Business Card</title>
<link rel="stylesheet" href="https://fonts.googleapis.com/css2?family=Lato:wght@300;400;700;900&display=swap">
<style>
  :root {
    --page-bg: #1a1a1a;
    --card-black: #0b0b0b;
    --card-edge: #2a2a2a;
    --band-white: #e4e4e4;
    --ink-dark: #1b1b1b;
    --text-white: #ffffff;
    --text-soft: #c9c9c9;
    --silver: #cfcfcf;
    --divider: #2c2c2c;
  }
  * { margin: 0; padding: 0; box-sizing: border-box; }
  html, body {
    width: 1200px;
    height: 900px;
    overflow: hidden;
    background: var(--page-bg);
    font-family: "Lato", sans-serif;
  }
  .canvas {
    width: 1200px;
    height: 900px;
    display: flex;
    flex-direction: column;
    align-items: center;
    justify-content: center;
    gap: 60px;
  }
  .card {
    position: relative;
    width: 630px;
    height: 360px;
    background: var(--card-black);
    border-radius: 20px;
    border: 1px solid var(--card-edge);
    overflow: hidden;
    box-shadow: 0 18px 40px rgba(0,0,0,0.55);
  }

  /* Back: appointment side */
  .brand-mark {
    position: absolute;
    left: 0;
    right: 0;
    top: 92px;
    display: flex;
    align-items: center;
    justify-content: center;
    gap: 14px;
  }
  .brand-mark .dot {
    width: 14px;
    height: 14px;
    border-radius: 50%;
    background: var(--silver);
  }
  .brand-mark .brand-name {
    color: var(--silver);
    font-weight: 700;
    font-size: 30px;
    letter-spacing: 4px;
    text-transform: uppercase;
  }
  .appointment-band {
    position: absolute;
    left: 0;
    right: 0;
    bottom: 52px;
    height: 86px;
    background: var(--band-white);
    display: flex;
    align-items: center;
    padding: 0 44px;
    gap: 18px;
  }
  .appointment-label {
    color: var(--ink-dark);
    font-weight: 700;
    font-size: 20px;
    letter-spacing: 0.5px;
    white-space: nowrap;
  }
  .appointment-line {
    flex: 1;
    height: 1px;
    background: var(--ink-dark);
    margin-top: 10px;
  }

  /* Front: contact side */
  .card-front {
    display: flex;
  }
  .front-mark {
    width: 300px;
    display: flex;
    align-items: center;
    justify-content: center;
    gap: 12px;
  }
  .front-mark .dot {
    width: 14px;
    height: 14px;
    border-radius: 50%;
    background: var(--text-white);
  }
  .front-mark .brand-name {
    color: var(--text-white);
    font-weight: 700;
    font-size: 24px;
    letter-spacing: 3px;
    text-transform: uppercase;
  }
  .front-divider {
    width: 1px;
    margin: 40px 0;
    background: var(--divider);
  }
  .contact {
    flex: 1;
    padding: 70px 0 0 38px;
    color: var(--text-white);
  }
  .contact-name {
    font-weight: 700;
    font-size: 25px;
    letter-spacing: 0.5px;
    text-transform: uppercase;
    line-height: 1.1;
  }
  .contact-title {
    font-weight: 300;
    font-size: 18px;
    color: var(--text-soft);
    margin-top: 2px;
  }
  .contact-phone {
    display: flex;
    align-items: center;
    gap: 8px;
    font-weight: 400;
    font-size: 19px;
    color: var(--text-soft);
    margin-top: 26px;
  }
  .contact-phone svg { width: 18px; height: 18px; fill: var(--text-white); }
  .contact-address {
    font-style: normal;
    font-weight: 400;
    font-size: 19px;
    color: var(--text-soft);
    line-height: 1.3;
    margin-top: 24px;
  }
</style>
</head>
<body>
<main class="canvas">

  <section class="card card-back" aria-label="Card back – next appointment">
    <div class="brand-mark">
      <span class="dot"></span>
      <span class="brand-name">Vintner Dental</span>
    </div>
    <div class="appointment-band">
      <span class="appointment-label">NEXT APPOINTMENT</span>
      <span class="appointment-line"></span>
    </div>
  </section>

  <section class="card card-front" aria-label="Card front – contact details">
    <div class="front-mark">
      <span class="dot"></span>
      <span class="brand-name">Vintner Dental</span>
    </div>
    <div class="front-divider"></div>
    <div class="contact">
      <h1 class="contact-name">Dr Marlo Vintner</h1>
      <p class="contact-title">Doctor of Dental Medicine</p>
      <p class="contact-phone">
        <svg viewBox="0 0 24 24" aria-hidden="true"><path d="M6.6 10.8a15.1 15.1 0 0 0 6.6 6.6l2.2-2.2a1 1 0 0 1 1-.25 11.4 11.4 0 0 0 3.6.57 1 1 0 0 1 1 1V20a1 1 0 0 1-1 1A17 17 0 0 1 3 4a1 1 0 0 1 1-1h3.5a1 1 0 0 1 1 1c0 1.25.2 2.45.57 3.57a1 1 0 0 1-.25 1z"/></svg>
        514-629-5074
      </p>
      <address class="contact-address">
        5182 Ch. Birchfield<br>
        Montreal QC H2T 4B9
      </address>
    </div>
  </section>

</main>
</body>
</html>
```